Ladies of Labour Global

We will be building the site using Rho Web Forge content management system so design needs to be RWF compatible including fonts used.
Client has a site already www.ladiesoflabourglobal.example
The overall look and feel desired by the client is for a professional yet social website. The website is to reflect the networking and professional training aspect of the clients business.
Pink and purple would be the dominant colours best used with white to maintain the clean professional feel.
Client likes www.galsincommerce.example as an example
Images to use should be anything networking and awards type, I have attached their logo.
Homepage Layout
- Banner across the top with logo top left
- Horizontal navigation bar
- Newsletter sign up in the banner area
- Join facebook/twitter
- A large area for rotating images
- A side panel for upcoming events/training
- Room to put sponsors logo’s across bottom of page.
Content page Layout
- Will not need the large area for rotating images
- Join Facebook/Twitter
- Room for content
- Side Panel to out in newsletter signup and upcoming events
Sitemap
o Home
o About Us
o History
o Events
? -International Women’s Day
? - Trailblazer Prize
? - Skills and Careers Fair
? - Rose Rally
? - Networking Gallery
o Membership
? - Why Join?
? - Membership Form
o Training
? - Computer Training
? - Function Planning Academy
? - QRS Youth Program
o Latest News
? - Media Articles
? - Current Newsletter
? - Links
o Blog
o Contact Us
Hi everyone
Thanks you so much for submitting designs, I will be presenting them to my client on Monday so will let you know feedback after that.
Cheers
Mara
Hi designers
We gave the designs to our client before xmas but due to xmas/new year break they haven't responded as yet. We get back on 10th January so we sould have a respose from them by then.
Thanks for your patience.
Cheers
Mara
Hi everyone
Thanks for your patience we have had some major flooding in SE QLD so has closed a lot of businesses down until yesterday, we are hoping to meet with our client this week to select a design.
Cheers
Mara
Hi everyone
I appreciate your patience with this project.....I am still waiting on my client to make a decision on design am hoping it will be next week so I can close this project.
Cheers
Mara
Hi everyone
I've finally heard back from the client who have now been caught in Cyclone Teru.....but they have told me they will be selecting a design next Tuesday so I will let you know outcome asap.
Apologies for the delay with this project.
Thanks
Mara

```html
<!DOCTYPE html>
<html lang="en">
<head>
<meta charset="utf-8">
<title>Ladies of Labour Global</title>
<link href="https://fonts.googleapis.com/css2?family=Libre+Baskerville:ital@0;1&family=Cabin:wght@400;500&family=Alegreya+Sans+SC:wght@500&family=Bebas+Neue&display=swap" rel="stylesheet">
<style>
:root{
  --pink:#c0308f;
  --pink-light:#d655ae;
  --pink-dark:#a81f7c;
  --navy:#2b3a7a;
  --text:#555;
  --rule:#c9c9c9;
  --placeholder:#a0a0a0;
  --white:#fff;
}
*{margin:0;padding:0;box-sizing:border-box}
html,body{width:1108px;height:1200px;overflow:hidden;background:var(--white)}
body{position:relative;font-family:"Libre Baskerville",Georgia,serif;color:var(--text)}
.abs{position:absolute}

.brand{left:152px;top:26px;width:130px;font-size:17px;line-height:20px;color:var(--navy);text-align:center;display:flex;align-items:center;gap:6px}
.brand-dot{width:14px;height:14px;border-radius:50%;background:var(--navy);flex:none}

.social{top:9px;display:flex;gap:9px;left:732px}
.social span{width:28px;height:28px;border-radius:5px;background:linear-gradient(#6b8fc4,#3b5f9c)}
.social span:last-child{background:linear-gradient(#7cc1d4,#3f8ea6)}

.contact{left:865px;top:-4px;width:127px;height:45px;border:4px solid var(--pink);border-radius:0 0 6px 6px;font-family:"Cabin",sans-serif;font-size:14px;color:var(--pink);display:flex;align-items:center;justify-content:center;padding-top:4px;letter-spacing:.3px}

.newsletter-label{left:545px;top:64px;font-size:13.5px;color:#666}
.newsletter-input{left:730px;top:59px;width:259px;height:27px;border:1px solid var(--pink);font-family:"Libre Baskerville",serif;font-size:12.5px;color:#666;padding:5px 7px}

.nav{left:0;top:101px;width:1108px;height:42px;background:linear-gradient(var(--pink-light),var(--pink-dark));border-top:2px solid #e07cc3;border-bottom:2px solid #e07cc3;display:flex;padding-left:120px}
.nav a{font-family:"Cabin",sans-serif;font-size:13px;color:var(--white);text-decoration:none;display:flex;align-items:center;justify-content:center;border-right:1px solid rgba(0,0,0,.15);letter-spacing:.3px}
.nav a.active{background:var(--white);color:var(--navy);margin-bottom:-2px}

.intro{left:0;top:160px;width:1108px;text-align:center;font-size:20px;line-height:30px;color:#555}
.intro-link{left:0;top:224px;width:1108px;text-align:center}
.intro-link a{font-style:italic;font-size:14.5px;color:var(--navy);text-decoration:none;border-bottom:1px solid var(--navy);padding-bottom:2px}

.rule{left:105px;width:887px;height:1px;background:var(--rule)}

.slider{left:104px;top:284px;width:887px;height:314px;border-radius:5px;overflow:hidden;background:linear-gradient(90deg,#e4ebef 0%,#c9d4dc 45%,#9eb0bc 100%)}
.slider-photo{left:0;top:0;width:410px;height:314px;background:radial-gradient(ellipse at 45% 55%,#f2f4f5 0%,#cfd9df 60%,rgba(207,217,223,0) 100%)}
.quote{left:412px;top:86px;font-family:"Bebas Neue",sans-serif;font-size:44px;line-height:48px;color:#f1f3f4;text-shadow:1px 1px 2px rgba(0,0,0,.25);letter-spacing:.5px}
.qmark{font-family:"Bebas Neue",sans-serif;font-size:110px;line-height:1;color:#f1f3f4;text-shadow:1px 1px 2px rgba(0,0,0,.25)}
.qmark.open{left:410px;top:18px}
.qmark.close{left:820px;top:192px}

.dots{left:482px;top:616px;display:flex;gap:13px}
.dots span{width:15px;height:15px;border-radius:50%;background:var(--navy)}
.dots span.on{background:var(--pink)}

.join{left:746px;top:626px;font-family:"Cabin",sans-serif;font-size:16.5px;color:var(--pink);display:flex;align-items:center;gap:8px}

.card{top:697px;width:190px}
.card-media{width:180px;height:91px;border-radius:4px;background:var(--placeholder)}
.card-badge{width:150px;height:112px;margin-top:-12px;margin-left:-2px;border-radius:50%;background:radial-gradient(circle,#d8efe2 0%,#bfe4cf 55%,#f7d0e8 100%)}
.card p{margin-top:31px;font-size:13.3px;line-height:22px;color:#555}
.card-badge + p{margin-top:22px}
.btn{display:inline-block;margin-top:11px;margin-left:-4px;width:105px;height:30px;border:2px solid #e58ccc;background:linear-gradient(var(--pink-light),var(--pink-dark));color:var(--white);font-family:"Cabin",sans-serif;font-size:13.5px;text-align:center;line-height:26px;letter-spacing:.3px}

.sponsors-title{left:109px;top:1036px;font-family:"Alegreya Sans SC",sans-serif;font-weight:500;font-size:22px;line-height:22px;color:var(--navy)}
.brace{left:224px;top:1014px}
.sponsor{top:1020px;width:82px;height:82px;border-radius:50%;background:var(--placeholder);color:var(--white);font-family:"Alegreya Sans SC",sans-serif;font-weight:500;font-size:16px;line-height:16px;display:flex;align-items:center;justify-content:center;text-align:center}

.copyright{left:0;top:1140px;width:1108px;text-align:center;font-size:13px;color:#666}
</style>
</head>
<body>

<header>
  <div class="abs brand"><span class="brand-dot"></span><span>Ladies of Labour Global</span></div>
  <div class="abs social" role="img" aria-label="Social network profile links"><span></span><span></span><span></span></div>
  <div class="abs contact">CONTACT US</div>
  <div class="abs newsletter-label">Sign up for our newsletter</div>
  <div class="abs newsletter-input">Enter email address</div>
</header>

<nav class="abs nav">
  <a class="active" style="width:84px">HOME</a>
  <a style="width:112px">ABOUT US</a>
  <a style="width:87px">STORY</a>
  <a style="width:95px">EVENTS</a>
  <a style="width:133px">MEMBERSHIP</a>
  <a style="width:110px">TRAINING</a>
  <a style="width:131px">LATEST NEWS</a>
  <a style="width:79px;border-right:none">BLOG</a>
</nav>

<div class="abs intro">Ladies of Labour Global is a membership organisation offering networking,<br>training and employment opportunities to women and the community.</div>
<div class="abs intro-link"><a>Learn more about us ...</a></div>
<div class="abs rule" style="top:263px"></div>

<section class="abs slider">
  <div class="abs slider-photo" role="img" aria-label="Photo of a woman doctor in a white coat with a stethoscope, arms crossed"></div>
  <div class="abs qmark open">“</div>
  <div class="abs quote">Women who make a difference<br>make all the difference for<br>other women...</div>
  <div class="abs qmark close">”</div>
</section>

<div class="abs dots"><span class="on"></span><span></span><span></span><span></span><span></span></div>
<div class="abs join">Become a member today
  <svg width="20" height="14" viewBox="0 0 20 14"><path d="M2 1l6 6-6 6M10 1l6 6-6 6" fill="none" stroke="#c0308f" stroke-width="3"/></svg>
</div>
<div class="abs rule" style="top:662px"></div>

<article class="abs card" style="left:112px">
  <div class="card-media" role="img" aria-label="Event photo"></div>
  <p>The 2010 IWD Festival was held between the 8th and 13th of March 2010 at the Harbourside Club and Coral Bay Arts Hall Brookvale.</p>
  <span class="btn">LEARN MORE</span>
</article>
<article class="abs card" style="left:342px">
  <div class="card-media" role="img" aria-label="Event photo"></div>
  <p>The 2010 IWD Festival was held between the 8th and 13th of March 2010 at the Harbourside Club and Coral Bay Arts Hall Brookvale.</p>
  <span class="btn">LEARN MORE</span>
</article>
<article class="abs card" style="left:575px">
  <div class="card-media" role="img" aria-label="Event photo"></div>
  <p>The 2010 IWD Festival was held between the 8th and 13th of March 2010 at the Harbourside Club and Coral Bay Arts Hall Brookvale.</p>
  <span class="btn">LEARN MORE</span>
</article>
<article class="abs card" style="left:808px">
  <div class="card-badge" role="img" aria-label="Festival badge"></div>
  <p>The 2010 IWD Festival was held between the 8th and 13th of March 2010 at the Harbourside Club and Coral Bay Arts Hall Brookvale.</p>
  <span class="btn">LEARN MORE</span>
</article>

<div class="abs rule" style="top:1000px"></div>

<section>
  <div class="abs sponsors-title">Featured<br>Sponsors</div>
  <svg class="abs brace" width="22" height="88" viewBox="0 0 22 88"><path d="M18 2C9 2 10 10 10 22S10 40 3 44c7 4 7 10 7 22s-1 20 8 20" fill="none" stroke="#c0308f" stroke-width="3.5"/></svg>
  <div class="abs sponsor" style="left:273px">Sponsor<br>Logo</div>
  <div class="abs sponsor" style="left:424px">Sponsor<br>Logo</div>
  <div class="abs sponsor" style="left:566px">Sponsor<br>Logo</div>
  <div class="abs sponsor" style="left:721px">Sponsor<br>Logo</div>
  <div class="abs sponsor" style="left:878px">Sponsor<br>Logo</div>
</section>

<div class="abs rule" style="top:1120px"></div>
<footer class="abs copyright">Copyright 2010 Ladies of Labour Global. All rights reserved</footer>

</body>
</html>
```